Copper Ridge Excursions Post Card/Flyer

Postcard/flyer needs to convey our mission: to provide an authentic, boutique wine tour of exceptional quality with first class customer service. It needs to be clean and high quality. Less is more :) Worthy of 5 star hotel concierges handing them to a guest. I provided an old flyer my friend made and my competitors flyer. Please use these just as reference, but i want to see your creativity. I like the format of "Meadow Harvest" -scan 91-flyer BUT I don't want to copy.
Updates

Need extra days to review

Target Market(s)

Couples, travelers, hotel employees, local industry, etc...

Industry/Entity Type

Boutique

Requirements
Must have
• Must have bullet points of the my previous reference flyer and any photos .Please use website for reference too.
• Revulo, route scout affirmations Plus Snapmora
• "Group and Private Tours available"
• "Mention this card for 10% off any tour" - low key please
• copperridgeexcursions.com, info@copperridgeexcursions.com, 805-618-2934
Nice to have
• clean lines , simple and elegant
• double sided please
Should not have
• Not too busy.

```html
<!DOCTYPE html>
<html lang="en">
<head>
<meta charset="utf-8">
<title>Copper Ridge Excursions – Postcard</title>
<link href="https://fonts.googleapis.com/css2?family=Open+Sans:wght@400;600&family=Tinos:wght@400&display=swap" rel="stylesheet">
<style>
  :root {
    --page-bg: #e9e7e3;
    --card-bg: #fbfbf8;
    --green: #2c5e3f;
    --green-dark: #24513a;
    --taupe: #8a7766;
    --text: #4a4a48;
    --line: #c9c9c6;
    --gold: #b59a6a;
  }
  * { box-sizing: border-box; margin: 0; padding: 0; }
  html, body { width: 940px; height: 1200px; overflow: hidden; }
  body {
    background: var(--page-bg);
    font-family: "Open Sans", Arial, sans-serif;
    color: var(--text);
    position: relative;
  }
  .postcard {
    position: absolute;
    left: 60px;
    width: 820px;
    height: 490px;
    background: var(--card-bg);
    box-shadow: 0 2px 6px rgba(0,0,0,0.18);
    display: flex;
  }
  .postcard--front { top: 60px; }
  .postcard--back { top: 620px; }

  /* Front */
  .front-gallery {
    width: 370px;
    height: 100%;
    display: flex;
    flex-direction: column;
    gap: 3px;
  }
  .photo-vineyard-rows {
    flex: 0 0 348px;
    background: linear-gradient(180deg, #8a9a7a 0%, #6f8f52 22%, #4f7a33 55%, #3c6426 100%);
  }
  .photo-strip { flex: 1; display: flex; gap: 3px; }
  .photo-couple { flex: 0 0 95px; background: linear-gradient(160deg, #c9b8a2, #8d6e58 60%, #5b4a3c); }
  .photo-grapes { flex: 0 0 185px; background: linear-gradient(160deg, #7a9a45, #3e5a2e 50%, #3a3850); }
  .photo-guests { flex: 1; background: linear-gradient(160deg, #9bb07e, #6b7f5a 55%, #4b5246); }

  .front-info {
    flex: 1;
    display: flex;
    flex-direction: column;
    align-items: center;
    padding-top: 48px;
  }
  .brand-name {
    font-family: "Tinos", "Times New Roman", serif;
    color: var(--green);
    font-size: 34px;
    line-height: 1.1;
    text-align: center;
    letter-spacing: 0.5px;
  }
  .brand-mark {
    width: 14px; height: 14px;
    background: var(--green);
    border-radius: 50%;
    margin-bottom: 10px;
  }
  .headline {
    font-family: "Tinos", "Times New Roman", serif;
    color: var(--green);
    font-size: 23px;
    line-height: 1.35;
    text-align: center;
    margin-top: 28px;
  }
  .headline-rule {
    width: 240px;
    height: 1px;
    background: var(--gold);
    margin: 12px 0 16px;
  }
  .intro {
    align-self: flex-start;
    margin-left: 24px;
    font-size: 13.5px;
  }
  .features {
    list-style: none;
    align-self: flex-start;
    margin: 12px 0 0 24px;
    font-size: 13.5px;
  }
  .features li {
    display: flex;
    align-items: center;
    gap: 10px;
    height: 24.5px;
  }
  .features svg { flex: none; }
  .offer {
    font-family: "Tinos", "Times New Roman", serif;
    color: var(--green);
    font-size: 16px;
    margin-top: 14px;
  }
  .phone-band {
    width: 100%;
    height: 32px;
    background: var(--green-dark);
    color: #fff;
    font-weight: 600;
    font-size: 15.5px;
    display: flex;
    align-items: center;
    justify-content: center;
    gap: 8px;
    margin-top: 6px;
    letter-spacing: 0.3px;
  }
  .website {
    font-size: 16px;
    font-weight: 600;
    color: #3d3d3b;
    letter-spacing: 0.4px;
    margin-top: 8px;
  }

  /* Back */
  .back-promo {
    width: 378px;
    display: flex;
    flex-direction: column;
    align-items: center;
    padding-top: 34px;
  }
  .back-promo .brand-name { font-size: 30px; }
  .photo-sunset-vineyard {
    width: 100%;
    height: 205px;
    margin-top: 30px;
    background: linear-gradient(180deg, #d9a76a 0%, #b98a55 25%, #7d7a3c 50%, #5d6b2a 75%, #8a9a33 100%);
  }
  .tours-available {
    font-size: 16.5px;
    font-weight: 600;
    color: var(--taupe);
    letter-spacing: 0.3px;
    margin-top: 10px;
  }
  .back-promo .offer { margin-top: 6px; }
  .back-promo .phone-band { margin-top: 10px; }

  .back-address {
    flex: 1;
    position: relative;
  }
  .sender {
    position: absolute;
    left: 22px;
    top: 26px;
    font-size: 11px;
    line-height: 1.4;
  }
  .stamp-box {
    position: absolute;
    right: 40px;
    top: 24px;
    width: 88px;
    height: 56px;
    border: 1.5px solid var(--line);
  }
  .address-line {
    position: absolute;
    left: 28px;
    right: 40px;
    height: 1.5px;
    background: var(--line);
  }
  .address-line:nth-of-type(1) { top: 210px; }
  .address-line:nth-of-type(2) { top: 252px; }
  .address-line:nth-of-type(3) { top: 294px; }
</style>
</head>
<body>

<section class="postcard postcard--front">
  <div class="front-gallery">
    <div class="photo-vineyard-rows" role="img" aria-label="Photo of vineyard rows stretching toward green hills"></div>
    <div class="photo-strip">
      <div class="photo-couple" role="img" aria-label="Photo of a couple enjoying wine at a tasting"></div>
      <div class="photo-grapes" role="img" aria-label="Photo of dark grape clusters on the vine"></div>
      <div class="photo-guests" role="img" aria-label="Photo of guests tasting wine outdoors with a guide"></div>
    </div>
  </div>

  <div class="front-info">
    <div class="brand-mark"></div>
    <div class="brand-name">Copper Ridge Excursions</div>
    <h1 class="headline">Come Explore Santa Barbara<br>Wine Country with us!</h1>
    <div class="headline-rule"></div>
    <p class="intro">An authentic and boutique wine tour experience</p>
    <ul class="features">
      <li><svg width="13" height="13" viewBox="0 0 13 13"><circle cx="6.5" cy="6.5" r="5.6" fill="none" stroke="#2c5e3f" stroke-width="1.3"/><path d="M5 4 L7.6 6.5 L5 9" fill="none" stroke="#2c5e3f" stroke-width="1.4"/></svg>Premium wine tasting at boutique wineries</li>
      <li><svg width="13" height="13" viewBox="0 0 13 13"><circle cx="6.5" cy="6.5" r="5.6" fill="none" stroke="#2c5e3f" stroke-width="1.3"/><path d="M5 4 L7.6 6.5 L5 9" fill="none" stroke="#2c5e3f" stroke-width="1.4"/></svg>Safe and comfortable luxury vehicles</li>
      <li><svg width="13" height="13" viewBox="0 0 13 13"><circle cx="6.5" cy="6.5" r="5.6" fill="none" stroke="#2c5e3f" stroke-width="1.3"/><path d="M5 4 L7.6 6.5 L5 9" fill="none" stroke="#2c5e3f" stroke-width="1.4"/></svg>Picnic lunch in vineyard setting</li>
      <li><svg width="13" height="13" viewBox="0 0 13 13"><circle cx="6.5" cy="6.5" r="5.6" fill="none" stroke="#2c5e3f" stroke-width="1.3"/><path d="M5 4 L7.6 6.5 L5 9" fill="none" stroke="#2c5e3f" stroke-width="1.4"/></svg>Local expert guides</li>
    </ul>
    <p class="offer">Mention this card for 10% off any tour</p>
    <div class="phone-band">
      <svg width="18" height="18" viewBox="0 0 18 18"><circle cx="9" cy="9" r="8" fill="none" stroke="#fff" stroke-width="1.3"/><path d="M6.2 4.8 L7.6 4.6 L8.3 6.8 L7.4 7.6 Q8.2 9.6 10.4 10.6 L11.2 9.7 L13.3 10.4 L13.1 11.8 Q10.6 13.2 7.6 10.4 Q4.8 7.4 6.2 4.8 Z" fill="#fff"/></svg>
      805 618 2934
    </div>
    <p class="website">www.copperridgeexcursions.com</p>
  </div>
</section>

<section class="postcard postcard--back">
  <div class="back-promo">
    <div class="brand-mark"></div>
    <div class="brand-name">Copper Ridge Excursions</div>
    <div class="photo-sunset-vineyard" role="img" aria-label="Photo of vineyard rows on rolling hills at golden sunset"></div>
    <p class="tours-available">GROUP AND PRIVATE TOURS AVAILABLE</p>
    <p class="offer">Mention this card for 10% off any tour</p>
    <div class="phone-band">
      <svg width="18" height="18" viewBox="0 0 18 18"><circle cx="9" cy="9" r="8" fill="none" stroke="#fff" stroke-width="1.3"/><path d="M6.2 4.8 L7.6 4.6 L8.3 6.8 L7.4 7.6 Q8.2 9.6 10.4 10.6 L11.2 9.7 L13.3 10.4 L13.1 11.8 Q10.6 13.2 7.6 10.4 Q4.8 7.4 6.2 4.8 Z" fill="#fff"/></svg>
      805 618 2934
    </div>
    <p class="website">www.copperridgeexcursions.com</p>
  </div>

  <div class="back-address">
    <address class="sender" style="font-style: normal;">
      42 Alder Lane,<br>
      Fernbrook TAS 7310<br>
      info@copperridgeexcursions.com
    </address>
    <div class="stamp-box"></div>
    <div class="address-line"></div>
    <div class="address-line"></div>
    <div class="address-line"></div>
  </div>
</section>

</body>
</html>
```